Tidewater Bureau for Crop Wellbeing and Harm Reduction Needs a Flyer Design

We need a flyer design template for our research, education, and prevention center housed at a major university called the "Tidewater Bureau for Crop Wellbeing and Harm Reduction (TBCWHR)." We would like to see designs that use the colors blue and white (PMS 286 (Pantone Matching System) with images that reflect farm scenes in the southeast. I've attached the TBCWHR logo, university logo and copy for the flyer. However, we are most interested in a design template that we can use again and again for new and updated information or for future flyers. This has to be a flyer that we can print on regular paper stock or glossy.
Professionals in agriculture professions; agriculture communities
University

```html
<!DOCTYPE html>
<html lang="en">
<head>
<meta charset="utf-8">
<title>Tidewater Bureau for Crop Wellbeing and Harm Reduction – Flyer</title>
<link rel="stylesheet" href="https://fonts.googleapis.com/css2?family=Arimo:wght@400;700&family=Tinos:wght@400;700&display=swap">
<style>
  :root {
    --pms-286: #0a4ea0;
    --pms-286-deep: #063f8a;
    --white: #ffffff;
    --page-bg: #e9eaec;
    --field-light: #9ad46a;
    --field-mid: #5eae3c;
    --field-deep: #2f7a22;
    --banner-lime: #a8cf2a;
    --banner-green: #3f8a22;
    --banner-dark: #255f18;
  }
  * { box-sizing: border-box; margin: 0; padding: 0; }
  html, body { width: 881px; height: 1200px; overflow: hidden; }
  body { background: var(--page-bg); font-family: "Arimo", Arial, sans-serif; position: relative; }

  .flyer {
    position: absolute; left: 109px; top: 62px; width: 680px; height: 960px;
    background: var(--white); box-shadow: 0 2px 10px rgba(0,0,0,.12);
  }

  .masthead { position: relative; height: 156px; }
  .university-name {
    position: absolute; left: 16px; top: 30px; width: 200px;
    font-family: "Tinos", "Times New Roman", serif; color: var(--pms-286);
  }
  .university-name .wordmark { font-size: 27px; line-height: 1.05; font-weight: 400; }
  .university-name .rule { height: 1px; background: var(--pms-286); margin: 8px 0 5px; opacity: .5; }
  .university-name .college { font-size: 16px; }

  .center-name {
    position: absolute; right: 18px; top: 24px; width: 112px; text-align: center;
    font-family: "Tinos", "Times New Roman", serif; color: var(--pms-286);
  }
  .center-name .mark { width: 40px; height: 40px; border-radius: 50%; background: var(--pms-286); margin: 0 auto 10px; }
  .center-name .acronym { font-size: 22px; font-weight: 700; letter-spacing: .5px; }

  .hero-photo {
    height: 324px;
    background:
      radial-gradient(ellipse 60% 45% at 55% 80%, rgba(200,235,230,.75), rgba(200,235,230,0) 70%),
      linear-gradient(180deg, var(--field-light) 0%, var(--field-mid) 55%, var(--field-deep) 100%);
  }

  .title-banner {
    height: 94px; padding: 20px 24px 0;
    background: linear-gradient(100deg, var(--banner-dark) 0%, var(--banner-green) 25%, var(--banner-lime) 50%, var(--banner-green) 75%, var(--banner-dark) 100%);
    color: var(--white); font-weight: 700;
  }
  .title-banner h1 { font-size: 23px; line-height: 30px; font-weight: 700; }
  .title-banner h1 .line-one { display: block; }
  .title-banner h1 .line-two { display: block; padding-left: 100px; }

  .info-panel { background: var(--pms-286); height: 322px; padding: 16px 16px 0; color: var(--white); }
  .section-head { position: relative; height: 20px; margin-bottom: 10px; }
  .section-head::before {
    content: ""; position: absolute; left: 0; right: 16px; top: 17px; height: 1px; background: var(--white);
  }
  .section-head::after {
    content: ""; position: absolute; right: 14px; top: 15px; width: 5px; height: 5px; border-radius: 50%; background: var(--white);
  }
  .pill {
    position: relative; z-index: 1; display: inline-block; height: 20px; padding: 0 16px 0 9px;
    background: var(--white); color: var(--pms-286); border-radius: 10px 10px 0 10px;
    font-family: "Tinos", "Times New Roman", serif; font-weight: 700; font-size: 13px; line-height: 20px;
  }
  .info-panel p { font-size: 10.5px; line-height: 14px; margin: 0 0 20px 8px; }
  .facts { list-style: none; margin-left: 8px; }
  .facts li { display: flex; align-items: center; font-size: 10.5px; height: 20px; }
  .facts svg { width: 12px; height: 12px; margin-right: 9px; flex: none; }

  .contact-strip {
    height: 39px; padding-top: 4px; text-align: center; color: var(--pms-286);
    font-size: 12px; line-height: 16px;
  }
  .contact-strip strong { font-weight: 700; }
  .base-band { height: 25px; background: var(--pms-286); }
</style>
</head>
<body>
  <article class="flyer">
    <header class="masthead">
      <div class="university-name">
        <div class="wordmark">Eastbrook State University</div>
        <div class="rule"></div>
        <div class="college">College of Public Health</div>
      </div>
      <div class="center-name">
        <div class="mark"></div>
        <div class="acronym">TBCWHR</div>
      </div>
    </header>

    <div class="hero-photo" role="img" aria-label="Farm worker in a wide hat spraying a green crop field, mist drifting across the rows"></div>

    <div class="title-banner">
      <h1><span class="line-one">Tidewater Bureau for</span><span class="line-two">Crop Wellbeing and Harm Reduction</span></h1>
    </div>

    <section class="info-panel">
      <div class="section-head"><span class="pill">What We Do…</span></div>
      <p>Research, education and advocacy to prevent work-related illnesses and injuries and injuries and to improve the safety and health of agricultural workers and their families in the southeastern United States.</p>

      <div class="section-head"><span class="pill">Who We Serve…</span></div>
      <p>Family farmers, farm workers, large producers, professionals working in agricultural health &amp; safety, researchers and communities.</p>

      <div class="section-head"><span class="pill">Did you know…</span></div>
      <ul class="facts">
        <li><svg viewBox="0 0 12 12"><circle cx="6" cy="6" r="6" fill="#fff"/><path d="M3.2 6.2 5.2 8.2 8.9 3.8" fill="none" stroke="#0a4ea0" stroke-width="1.6"/></svg>Agriculture ranks among the most hazardous industries.</li>
        <li><svg viewBox="0 0 12 12"><circle cx="6" cy="6" r="6" fill="#fff"/><path d="M3.2 6.2 5.2 8.2 8.9 3.8" fill="none" stroke="#0a4ea0" stroke-width="1.6"/></svg>Agricultural injuries and deaths affect individuals, their families, and their communities.</li>
        <li><svg viewBox="0 0 12 12"><circle cx="6" cy="6" r="6" fill="#fff"/><path d="M3.2 6.2 5.2 8.2 8.9 3.8" fill="none" stroke="#0a4ea0" stroke-width="1.6"/></svg>Many of the more than 250 persons killed each year in farming related incidents include children, youth and older workers.</li>
        <li><svg viewBox="0 0 12 12"><circle cx="6" cy="6" r="6" fill="#fff"/><path d="M3.2 6.2 5.2 8.2 8.9 3.8" fill="none" stroke="#0a4ea0" stroke-width="1.6"/></svg>The annual estimated cost of agricultural injuries exceeds $4.5 billion.</li>
        <li><svg viewBox="0 0 12 12"><circle cx="6" cy="6" r="6" fill="#fff"/><path d="M3.2 6.2 5.2 8.2 8.9 3.8" fill="none" stroke="#0a4ea0" stroke-width="1.6"/></svg>1 in 10 workers in agriculture, forestry and commercial fishing is injured seriously enough to require time off.</li>
        <li><svg viewBox="0 0 12 12"><circle cx="6" cy="6" r="6" fill="#fff"/><path d="M3.2 6.2 5.2 8.2 8.9 3.8" fill="none" stroke="#0a4ea0" stroke-width="1.6"/></svg>Leading causes of death include tractors, machinery, motor vehicles, and electrocution.</li>
      </ul>
    </section>

    <footer>
      <div class="contact-strip">
        Visit us at <strong>www.tbcwhr.esu.edu</strong> and look for us on <strong>Fieldfeed</strong> and <strong>Chirpline</strong> or<br>
        <strong>CALL</strong> us at <strong>555.014.2290.</strong>
      </div>
      <div class="base-band"></div>
    </footer>
  </article>
</body>
</html>
```